Brisk Refrigeration. Refrigeration and air conditioning specialists.

We need a website to promote our business. We would a modern simple design using the colours from our logo and black. We want it to be fun but proffesional.

Target Market(s)

Commercial

Number of Pages Required

4 page

Requirements
Must have
• Home Page, About Us, Services and Contact Us.
• 24/7 365 days service available.
• Brisk Refrigeration's dedicated team specialises in commercial refrigeration and air conditioning equipment.
• Based in Harbourview, we cover Bayside Metro and surrounding areas.
Nice to have
• KNOWLEDGE . EXPERIENCE . PASSION in bold.
• Our experienced and highly trained technicians provide extensive knowledge and exceptional skills for your commercial refrigeration and air conditioning requirements.
• Pictures of commercial refrigeration.
Should not have
• No mention of domestic services.

```html
<!DOCTYPE html>
<html lang="en">
<head>
<meta charset="utf-8">
<title>Brisk Refrigeration</title>
<link rel="stylesheet" href="https://fonts.googleapis.com/css2?family=Roboto:wght@300;400;500;700;900&family=Roboto+Condensed:wght@500;700&family=Jost:wght@300;400&family=Montserrat:wght@400;600;700&display=swap">
<style>
:root{
  --purple:#3e2362;
  --purple-deep:#361d57;
  --green:#9ef26a;
  --ink:#2b2b2b;
  --text:#555;
  --footer:#2c2c2c;
  --white:#fff;
  --line:#c9c9c9;
}
*{box-sizing:border-box;margin:0;padding:0}
html,body{width:1200px;height:3358px;overflow:hidden}
body{position:relative;background:var(--white);font-family:"Roboto",sans-serif;color:var(--text)}
.abs{position:absolute}

/* header */
.site-header{position:absolute;left:0;top:0;width:1200px;height:141px;background:var(--white)}
.top-line{position:absolute;left:975px;top:0;width:225px;height:4px;background:var(--green)}
.top-bar{position:absolute;left:700px;top:0;width:275px;height:34px}
.top-phone{position:absolute;left:726px;top:0;height:34px;display:flex;align-items:center;gap:8px;color:var(--white);font-size:14px;font-weight:700;font-family:"Roboto",sans-serif;white-space:nowrap}
.brand{position:absolute;left:94px;top:26px;color:var(--green);font-weight:900;font-family:"Roboto",sans-serif;line-height:1}
.brand .name{font-size:58px;letter-spacing:1px}
.brand .sub{font-size:14px;letter-spacing:1px;margin-top:4px}
.nav{position:absolute;left:546px;top:78px;display:flex;align-items:center;font-family:"Montserrat",sans-serif;font-size:15px;color:var(--purple)}
.nav a{text-decoration:none;color:var(--purple);padding:3px 16px}
.nav .active{background:var(--purple);color:var(--white);border-radius:14px;font-weight:700;padding:3px 18px}
.nav .sep{color:#999;padding:0 8px}
.badge{position:absolute;left:1008px;top:40px;width:112px;height:60px;color:var(--purple)}
.badge .dot{position:absolute;left:40px;top:0;width:32px;height:32px;border-radius:50%;background:var(--purple)}
.badge .big{position:absolute;left:0;top:36px;font-family:"Roboto Condensed",sans-serif;font-weight:700;font-size:22px}
.badge .days{position:absolute;left:50px;top:36px;font-family:"Roboto Condensed",sans-serif;font-weight:700;font-size:13px;line-height:1}
.badge .note{position:absolute;left:50px;top:50px;font-size:6px;font-weight:700}

/* hero */
.hero{position:absolute;left:0;top:141px;width:1200px;height:699px;background:linear-gradient(120deg,#3a3d48 0%,#2a2c35 35%,#4a3f3a 60%,#2c2e38 100%)}
.hero-shade{position:absolute;inset:0;background:rgba(20,20,28,.45)}
.hero-lead{position:absolute;top:188px;width:100%;text-align:center;color:var(--white);font-family:"Jost",sans-serif;font-weight:300;font-size:38px}
.hero-title{position:absolute;top:242px;width:100%;text-align:center;color:var(--white);font-family:"Roboto Condensed",sans-serif;font-weight:700;font-size:56px;line-height:70px;letter-spacing:.5px}
.hero-tag{position:absolute;top:380px;width:100%;text-align:center;color:var(--green);font-family:"Roboto Condensed",sans-serif;font-weight:700;font-size:45px;letter-spacing:1px}
.btn-more{position:absolute;left:506px;top:475px;width:193px;height:42px;background:var(--green);color:var(--purple);border-radius:3px;font-family:"Roboto Condensed",sans-serif;font-weight:500;font-size:22px;display:flex;align-items:center;justify-content:center}
.hero-arrow{position:absolute;top:306px}
.dots{position:absolute;top:635px;left:572px;display:flex;gap:10px}
.dots span{width:11px;height:11px;border-radius:50%;border:2px solid var(--white)}
.dots .on{background:var(--white)}

/* about */
.section-title{font-family:"Roboto",sans-serif;font-weight:700;font-size:34px}
.rule{height:2px;width:70px}
.about-title{position:absolute;left:132px;top:938px;color:var(--purple)}
.about-rule{position:absolute;left:132px;top:988px;background:#bbb}
.about-copy{position:absolute;left:132px;top:1018px;width:450px;font-size:12.5px;line-height:19px;color:var(--text)}
.about-copy p{margin-bottom:19px}
.tech-photo{position:absolute;left:700px;top:885px;width:420px;height:615px;background:linear-gradient(180deg,#e9ecf1 0%,#3a4f85 45%,#23335e 100%);border-radius:200px 200px 0 0}

/* services */
.services{position:absolute;left:0;top:1500px;width:1200px;height:690px;background:var(--purple)}
.services-title{position:absolute;top:72px;width:100%;text-align:center;color:var(--green)}
.services-rule{position:absolute;left:565px;top:128px;background:rgba(255,255,255,.5)}
.services-intro{position:absolute;top:160px;width:100%;text-align:center;color:#e0d8ec;font-size:12.5px;line-height:25px}
.card{position:absolute;top:264px;width:228px}
.card .pic{width:228px;height:202px;background:var(--white);display:flex;align-items:center;justify-content:center}
.card .pic div{width:160px;height:150px}
.card h3{margin-top:22px;text-align:center;color:var(--green);font-family:"Montserrat",sans-serif;font-weight:700;font-size:16px}
.btn-service{position:absolute;left:524px;top:578px;width:152px;height:38px;background:var(--green);color:var(--purple);font-family:"Montserrat",sans-serif;font-weight:600;font-size:11px;display:flex;align-items:center;justify-content:center}

/* contact */
.contact-title{position:absolute;top:2282px;width:100%;text-align:center;color:var(--purple)}
.contact-rule{position:absolute;left:565px;top:2338px;background:#bbb}
.field-label{position:absolute;font-size:13px;color:var(--text)}
.field-label b{color:var(--purple);margin-left:6px}
.field{position:absolute;border:1px solid var(--line);background:var(--white)}
.req{position:absolute;left:674px;top:2562px;font-size:12px;color:var(--purple)}
.check{position:absolute;left:674px;top:2603px;display:flex;align-items:center;gap:14px;font-size:13px;color:var(--text)}
.check span{width:15px;height:15px;border:1px solid #999}
.btn-submit{position:absolute;left:531px;top:2689px;width:136px;height:36px;background:var(--purple);color:var(--white);border-radius:3px;font-family:"Roboto",sans-serif;font-weight:500;font-size:17px;display:flex;align-items:center;justify-content:center;letter-spacing:.5px}

/* newsletter */
.newsletter{position:absolute;left:0;top:2806px;width:1200px;height:154px;background:var(--green)}
.newsletter h2{position:absolute;left:175px;top:62px;font-size:24px;font-weight:700;color:var(--purple);letter-spacing:.5px}
.news-input{position:absolute;left:383px;top:55px;width:504px;height:50px;background:var(--white)}
.btn-subscribe{position:absolute;left:887px;top:55px;width:127px;height:50px;background:var(--purple);color:var(--white);font-size:14px;font-weight:700;display:flex;align-items:center;justify-content:center}

/* footer */
.footer{position:absolute;left:0;top:2960px;width:1200px;height:320px;background:var(--footer);color:var(--white)}
.footer-brand{position:absolute;left:112px;top:104px;color:var(--white);font-weight:900;line-height:1;text-align:center}
.footer-brand .name{font-size:62px;letter-spacing:1px}
.footer-brand .sub{font-size:15px;margin-top:6px;letter-spacing:1px}
.footer h4{position:absolute;top:66px;color:var(--green);font-size:17px;font-weight:700}
.foot-item{position:absolute;left:394px;font-size:14px;line-height:19px}
.foot-item .k{color:var(--green);font-weight:700}
.foot-links{position:absolute;left:630px;top:116px;list-style:none;font-size:14px}
.foot-links li{height:33px}
.foot-field{position:absolute;background:var(--white);color:#999;font-size:13px;padding-left:12px;display:flex;align-items:center}
.btn-send{position:absolute;left:795px;top:204px;width:130px;height:38px;background:var(--green);color:var(--purple);font-weight:700;font-size:15px;display:flex;align-items:center;justify-content:center}
.copyright{position:absolute;left:0;top:3280px;width:1200px;height:78px;background:var(--purple-deep);color:#cfc6de;font-size:12px;display:flex;align-items:center;justify-content:center}
</style>
</head>
<body>

<header class="site-header">
  <div class="top-line"></div>
  <svg class="top-bar" width="275" height="34" viewBox="0 0 275 34">
    <polygon points="0,0 178,0 178,34 20,34" fill="#3e2362"/>
    <polygon points="178,0 275,0 258,34 178,34" fill="#9ef26a"/>
  </svg>
  <div class="top-phone">
    <svg width="18" height="18" viewBox="0 0 20 20"><circle cx="10" cy="10" r="9" fill="none" stroke="#fff" stroke-width="1.6"/><path d="M7 5.5l1.6 2.3-1 1.2c.6 1.3 1.6 2.3 2.9 2.9l1.2-1 2.3 1.6-.8 1.8c-3.7-.3-6.7-3.3-7-7z" fill="#fff"/></svg>
    1-888-555-0147
  </div>

  <div class="brand"><div class="name">BRISK</div><div class="sub">REFRIGERATION</div></div>

  <nav class="nav">
    <a class="active">Home</a><span class="sep">|</span>
    <a>About Us</a><span class="sep">|</span>
    <a>Services</a><span class="sep">|</span>
    <a>Contact Us</a>
  </nav>

  <div class="badge">
    <div class="dot"></div>
    <div class="big">24/7</div>
    <div class="days">365 DAYS</div>
    <div class="note">SERVICE AVAILABLE</div>
  </div>
</header>

<section class="hero" role="img" aria-label="Technicians servicing an outdoor air conditioning unit">
  <div class="hero-shade"></div>
  <div class="hero-lead">Our dedicated team specialises in</div>
  <div class="hero-title">COMMERCIAL REFRIGERATION &amp;<br>AIR CONDITIONING EQUIPMENT.</div>
  <div class="hero-tag">KNOWLEDGE • EXPERIENCE • PASSION</div>
  <div class="btn-more">KNOW MORE</div>
  <svg class="hero-arrow" style="left:60px" width="26" height="48" viewBox="0 0 26 48"><polyline points="22,2 4,24 22,46" fill="none" stroke="rgba(255,255,255,.6)" stroke-width="2.5"/></svg>
  <svg class="hero-arrow" style="left:1112px" width="26" height="48" viewBox="0 0 26 48"><polyline points="4,2 22,24 4,46" fill="none" stroke="rgba(255,255,255,.6)" stroke-width="2.5"/></svg>
  <div class="dots"><span class="on"></span><span></span><span></span></div>
</section>

<section class="about">
  <h2 class="section-title about-title">About us</h2>
  <div class="rule about-rule"></div>
  <div class="about-copy">
    <p>Brisk Refrigeration's dedicated team specialises in commercial refrigeration and air conditioning equipment. Based in Harbourview, we cover Bayside Metro and surrounding areas.</p>
    <p>Lorem ipsum dolor sit amet, consectetur adipiscing elit. Quid autem habent admirationis, cum prope accesseris? An hoc usque quaque, aliter in vita? Non igitur de improbo, sed de callido improbo quaerimus, qualis Q. Nam quibus rebus efficiuntur voluptates, eae non sunt in potestate sapientis. Negare non possum. Huic mori optimum esse propter desperationem sapientiae, illi propter spem vivere. Quid enim me prohiberet Epicureum esse, si probarem, quae ille diceret? Qui-vere falsone, quaerere mittimus-dicitur oculis se privasse.</p>
    <p>Varietates autem iniurasque fortunae facile veteres philosophorum praeceptis instituta vita superabat. Et quod est munus, quod opus sapientiae! Non modo carum sibi quemque, verum etiam vehementer carum esse? Tu enim ista lenius, hic Stoicorum more nos vexat. Collatio igitur ista te nihil iuvat. Videamus animi partes, quarum est conspectus illustrior.</p>
  </div>
  <div class="tech-photo" role="img" aria-label="Smiling refrigeration technician in uniform holding a clipboard"></div>
</section>

<section class="services">
  <h2 class="section-title services-title">Our Services</h2>
  <div class="rule services-rule"></div>
  <p class="services-intro">Whether you wish to cool, store or display food and drink, we have a wide range of commercial refrigerator services catering to various small and large scale industries.<br>We specialize in wide range of commercial refrigeration operations and maintenance services to ensure efficient functioning of the systems.</p>

  <div class="card" style="left:119px"><div class="pic"><div role="img" aria-label="Commercial chest freezer" style="background:linear-gradient(180deg,#f2f3f5,#c9ccd2)"></div></div><h3>Commercial Freezer</h3></div>
  <div class="card" style="left:365px"><div class="pic"><div role="img" aria-label="Walk-in cooler room" style="background:linear-gradient(180deg,#e4e5e7,#b8babd)"></div></div><h3>Walk In Cooler</h3></div>
  <div class="card" style="left:611px"><div class="pic"><div role="img" aria-label="Stainless steel kitchen refrigerator" style="background:linear-gradient(180deg,#d9dbde,#9ea2a8)"></div></div><h3>Kitchen Refrigeration</h3></div>
  <div class="card" style="left:858px"><div class="pic"><div role="img" aria-label="Glass door drinks merchandiser" style="background:linear-gradient(180deg,#2d3a55,#1a2132)"></div></div><h3>Glass Door Merchandiser</h3></div>

  <div class="btn-service">MORE SERVICE</div>
</section>

<section class="contact">
  <h2 class="section-title contact-title">Contact Us</h2>
  <div class="rule contact-rule"></div>

  <div class="field-label" style="left:152px;top:2394px">Name<b>*</b></div>
  <div class="field" style="left:152px;top:2418px;width:396px;height:38px"></div>
  <div class="field-label" style="left:152px;top:2479px">Email<b>*</b></div>
  <div class="field" style="left:152px;top:2503px;width:396px;height:38px"></div>
  <div class="field-label" style="left:152px;top:2565px">Phone</div>
  <div class="field" style="left:152px;top:2588px;width:396px;height:38px"></div>

  <div class="field-label" style="left:674px;top:2394px">Description</div>
  <div class="field" style="left:674px;top:2418px;width:396px;height:132px"></div>
  <div class="req">* Required</div>
  <div class="check"><span></span>I have read the Disclaimer and Privacy Policy</div>

  <div class="btn-submit">SUBMIT</div>
</section>

<section class="newsletter">
  <h2>NEWSLETTER</h2>
  <div class="news-input"></div>
  <div class="btn-subscribe">SUBSCRIBE</div>
</section>

<footer class="footer">
  <div class="footer-brand"><div class="name">BRISK</div><div class="sub">REFRIGERATION</div></div>

  <h4 style="left:358px">CONTACT US</h4>
  <svg class="abs" style="left:358px;top:110px" width="24" height="32" viewBox="0 0 24 32"><path d="M12 1C6 1 2 5.5 2 11c0 7.5 10 20 10 20s10-12.5 10-20C22 5.5 18 1 12 1z" fill="#9ef26a"/><circle cx="12" cy="11" r="4" fill="#2c2c2c"/></svg>
  <div class="foot-item" style="top:108px"><div class="k">ADDRESS</div>4120 Willow Bend Road<br>Fairview, Alaska 34580</div>
  <svg class="abs" style="left:358px;top:190px" width="24" height="24" viewBox="0 0 24 24"><path d="M5 2l4 5-2.5 3c1.5 3 4 5.5 7 7l3-2.5 5 4-2 4C10 22 2 14 1.5 4z" fill="#9ef26a"/></svg>
  <div class="foot-item" style="top:190px"><div class="k">PHONE NUMBER</div>1-888-555-0147</div>

  <h4 style="left:625px">ABOUT</h4>
  <ul class="foot-links"><li>Home</li><li>About Us</li><li>Services</li><li>Contact us</li></ul>

  <h4 style="left:790px">GET IN TOUCH</h4>
  <div class="foot-field" style="left:795px;top:107px;width:150px;height:36px">Name</div>
  <div class="foot-field" style="left:954px;top:107px;width:150px;height:36px">Phone</div>
  <div class="foot-field" style="left:795px;top:150px;width:309px;height:38px">Email address</div>
  <div class="btn-send">SEND</div>
</footer>

<div class="copyright">© 2018 briskrefrigeration All Right Reserved</div>

</body>
</html>
```